Velmora Intergrated Marketing Stationary Design Contest

We require a very professional looking stationary set to include: letterhead, compliments slip and business cards (double sided bus cards).

Files should be supplied on either Illustrator or InDesign.

We are interested in perhaps encorporating a faint watermark with the letter q or the logo, but it isnt a pre-requisite

Target Market(s)

Business owners seeking professional marketing services

Industry/Entity Type

Marketing

Requirements
Must have
• Concurrent theme wiht business cards, letterhead and comp slip. Must be an editable document for future ammendment
Should not have
• No use of times new roman or similar fonts

```html
<!DOCTYPE html>
<html lang="en">
<head>
<meta charset="utf-8">
<title>Velmora Intergrated Marketing – Compliments Slip</title>
<link href="https://fonts.googleapis.com/css2?family=Mulish:wght@300;400&display=swap" rel="stylesheet">
<style>
  :root {
    --brand-orange: #f15a2b;
    --ink: #1a1a1a;
    --paper: #ffffff;
  }
  html, body {
    margin: 0;
    padding: 0;
    overflow: hidden;
    background: var(--paper);
  }
  .slip {
    position: relative;
    width: 1200px;
    height: 566px;
    background: var(--paper);
    font-family: "Mulish", Arial, sans-serif;
    font-weight: 300;
    color: var(--ink);
    overflow: hidden;
  }
  .brand {
    position: absolute;
    top: 57px;
    right: 57px;
    display: flex;
    align-items: center;
    gap: 14px;
  }
  .brand-name {
    color: var(--brand-orange);
    font-size: 26px;
    font-weight: 400;
  }
  .brand-dot {
    width: 114px;
    height: 114px;
    border-radius: 50%;
    background: var(--brand-orange);
  }
  .contact {
    position: absolute;
    left: 57px;
    top: 252px;
    margin: 0;
    font-size: 21px;
    line-height: 24px;
  }
  .contact-row {
    display: flex;
  }
  .contact-label {
    color: var(--brand-orange);
    width: 29px;
  }
  .address {
    position: absolute;
    left: 57px;
    top: 366px;
    margin: 0;
    font-style: normal;
    font-size: 20px;
    line-height: 24px;
  }
  .company-name {
    color: var(--brand-orange);
  }
  .legal {
    position: absolute;
    left: 57px;
    top: 455px;
    margin: 0;
    font-size: 15.5px;
    line-height: 19.5px;
  }
  .legal-label {
    color: var(--brand-orange);
  }
</style>
</head>
<body>
  <main class="slip">
    <div class="brand">
      <span class="brand-name">Velmora</span>
      <span class="brand-dot" aria-hidden="true"></span>
    </div>

    <div class="contact">
      <div class="contact-row"><span class="contact-label">T</span><span>01632 960614</span></div>
      <div class="contact-row"><span class="contact-label">F</span><span>01632 960611</span></div>
      <div class="contact-row"><span class="contact-label">E</span><span>enquiries@velmoraim.co.uk</span></div>
      <div class="contact-row"><span class="contact-label">W</span><span>www.velmoraim.co.uk</span></div>
    </div>

    <address class="address">
      <div class="company-name">Velmora Intergrated Marketing</div>
      <div>Harbour Offices, Mill Street,</div>
      <div>Thornbridge, West Yorkshire, TB4 7QX</div>
    </address>

    <div class="legal">
      <div><span class="legal-label">Company Registration</span> 4817305</div>
      <div><span class="legal-label">Vat No</span> 718 2045 61</div>
      <div>Trading as a division of Brantwell Ltd</div>
    </div>
  </main>
</body>
</html>
```